Business card design needed

I would like a one sided black business card with the information provided above. Refer to my website www.brightvolleyracquet.com.au for an example of colors I have used for my site, would like to keep this consistent for my business cards also, I will upload my logo below.

I am a new small business that provides tennis customers with racquet re stringing, tennis strings and accessories.

Industry/Entity Type

Small Business

Contact Information for Business Card

Bright Volley Racquet

Derek Fenwick
Managing Director

brightvolleyracquet@mailnest.com
www.brightvolleyracquet.com.au
0471 629 305

Racquet Restringing/Tennis Strings/Accessories

Requirements
Must have
• Must have my logo and card must be black

```html
<!DOCTYPE html>
<html lang="en">
<head>
<meta charset="utf-8">
<title>Bright Volley Racquet – Business Card</title>
<link rel="stylesheet" href="https://fonts.googleapis.com/css2?family=Cabin:ital,wght@0,400;0,500;1,400&display=swap">
<style>
  :root {
    --page-bg: #2a2a2a;
    --card-black: #0b0a0a;
    --card-glow: #2a2727;
    --lime: #c8e01e;
    --white: #f2f2f2;
    --grey: #b9b4ae;
    --sand: #d8c9b0;
    --blue: #3a8fd8;
    --text-font: "Cabin", "Gill Sans", sans-serif;
  }
  * { margin: 0; padding: 0; box-sizing: border-box; }
  html, body {
    width: 1200px;
    height: 949px;
    overflow: hidden;
    background: var(--page-bg);
    font-family: var(--text-font);
  }
  .stage {
    width: 1200px;
    height: 949px;
    display: flex;
    align-items: center;
    justify-content: center;
  }
  .business-card {
    position: relative;
    width: 1000px;
    height: 534px;
    background: radial-gradient(ellipse at 32% 30%, var(--card-glow) 0%, var(--card-black) 62%);
    box-shadow: 0 12px 40px rgba(0,0,0,0.55);
  }
  .brand {
    position: absolute;
    left: 79px;
    top: 120px;
    display: flex;
    align-items: center;
    gap: 18px;
  }
  .brand-dot {
    width: 56px;
    height: 56px;
    border-radius: 50%;
    background: var(--lime);
  }
  .brand-name {
    color: var(--lime);
    font-size: 34px;
    font-weight: 500;
    letter-spacing: 0.5px;
  }
  .contact {
    position: absolute;
    right: 78px;
    top: 78px;
    text-align: right;
  }
  .person-name {
    color: var(--white);
    font-size: 40px;
    font-weight: 400;
    line-height: 1.1;
  }
  .person-role {
    color: var(--lime);
    font-size: 24px;
    font-style: italic;
    margin-top: 2px;
  }
  .email {
    color: var(--grey);
    font-size: 26px;
    margin-top: 46px;
  }
  .phone {
    display: flex;
    align-items: center;
    justify-content: flex-end;
    gap: 16px;
    color: var(--sand);
    font-size: 36px;
    margin-top: 10px;
  }
  .phone-icon { width: 42px; height: 42px; }
  .services {
    position: absolute;
    left: 79px;
    top: 318px;
    list-style: none;
  }
  .services li {
    display: flex;
    align-items: center;
    gap: 16px;
    color: var(--white);
    font-size: 27px;
    font-style: italic;
    line-height: 40px;
  }
  .services li::before {
    content: "";
    width: 16px;
    height: 16px;
    border-radius: 50%;
    background: radial-gradient(circle at 35% 35%, #9fd0ff 0%, var(--blue) 60%, #1b4f86 100%);
  }
  .website {
    position: absolute;
    right: 62px;
    top: 428px;
    font-size: 20px;
    color: var(--white);
    letter-spacing: 0.5px;
  }
  .website .domain { color: var(--blue); }
</style>
</head>
<body>
<main class="stage">
  <article class="business-card">
    <div class="brand">
      <span class="brand-dot"></span>
      <span class="brand-name">Bright Volley Racquet</span>
    </div>

    <div class="contact">
      <p class="person-name">Derek Fenwick</p>
      <p class="person-role">Managing Director</p>
      <p class="email">brightvolleyracquet@mailnest.com</p>
      <p class="phone">
        <span>0471 629 305</span>
        <svg class="phone-icon" viewBox="0 0 42 42" aria-hidden="true">
          <circle cx="21" cy="21" r="19" fill="none" stroke="#d8c9b0" stroke-width="2"/>
          <path d="M15 11c1.5-1 3-.6 3.6.6l1.6 3.4c.4 1-.1 2-1 2.5l-1.4.8c.9 2.7 2.8 4.9 5.3 6.2l1-1.3c.6-.8 1.7-1.1 2.6-.6l3.2 1.9c1.1.7 1.3 2.2.4 3.4-1.2 1.6-3.2 2.4-5.2 1.6-5.5-2.2-9.4-6.6-11-12.3-.5-2.1.4-4.5 1.9-5.6z" fill="#d8c9b0"/>
        </svg>
      </p>
    </div>

    <ul class="services">
      <li>Racquet Restringing</li>
      <li>Tennis Strings</li>
      <li>Accessories</li>
    </ul>

    <p class="website">www.<span class="domain">brightvolleyracquet</span>.com.au</p>
  </article>
</main>
</body>
</html>
```